Corvelle Strategies business card

I need a business card for my new strategic consulting LLC, Corvelle Strategies. We specialize in helping people who care about broadband technology and telecommunications policy, and we're based in Washington DC. I'm looking for a card that says smart, credible, future-facing and signals a high level of expertise. It's DC, so there's clearly a limit to how crazy we can go with this card, but I am looking for a design that reflects a company that is comfortable with technology, policy, and having a little bit fun. I'm uploading my logo below, and I'd like to have it be part of the card design in some fashion.
Target Market(s)
Telecommunications and technology policy professionals
Industry/Entity Type
Technology policy
Contact Information for Business Card
Name of business, my name (Glen Mosswater), email (glen@corvellestrategies-example.com) , phone number (202-555-0148)phone number

```html
<!DOCTYPE html>
<html lang="en">
<head>
<meta charset="UTF-8">
<title>Corvelle Strategies — Business Card</title>
<link href="https://fonts.googleapis.com/css2?family=Poppins:wght@400;500;600&display=swap" rel="stylesheet">
<style>
  :root {
    --backdrop: #979797;
    --card: #ffffff;
    --navy: #0b4ea2;
    --blue: #1d5fc0;
    --gold: #f7aa3a;
    --ink: #1b1b1b;
    --globe-light: #a9c1f0;
    --globe-deep: #6f97e6;
    --net: #dfe8f5;
  }
  * { margin: 0; padding: 0; box-sizing: border-box; }
  html, body {
    width: 965px; height: 1200px; overflow: hidden;
    background: var(--backdrop);
    font-family: "Poppins", sans-serif;
  }
  .card {
    position: absolute; left: 171px; width: 623px; height: 355px;
    background: var(--card); overflow: hidden;
  }
  .card--front { top: 168px; }
  .card--back { top: 666px; }

  .network {
    position: absolute; border-radius: 50%;
    background: radial-gradient(closest-side, var(--net), rgba(223,232,245,0));
  }
  .network--upper { left: -60px; top: -90px; width: 420px; height: 380px; }
  .network--lower { left: 280px; top: 150px; width: 420px; height: 300px; }

  .wordmark {
    position: absolute; display: flex; align-items: center; gap: 10px;
    color: var(--navy); font-weight: 600; white-space: nowrap;
  }
  .wordmark__sun { border-radius: 50%; background: var(--gold); flex: none; }
  .card--front .wordmark {
    left: 0; right: 0; top: 112px; justify-content: center; font-size: 38px; letter-spacing: -0.5px;
  }
  .card--front .wordmark__sun { width: 26px; height: 26px; }
  .divider {
    position: absolute; left: 276px; top: 204px; width: 71px; height: 1px; background: var(--gold);
  }
  .tagline {
    position: absolute; left: 0; right: 0; top: 216px; text-align: center;
    color: var(--blue); font-size: 11.5px; letter-spacing: 2.2px; font-weight: 400;
  }
  .tagline .dot { color: var(--gold); }

  .card--back .wordmark { left: 46px; top: 88px; font-size: 23px; letter-spacing: -0.3px; gap: 7px; }
  .card--back .wordmark__sun { width: 16px; height: 16px; }
  .person {
    position: absolute; left: 50px; top: 166px; display: flex; align-items: center; gap: 8px;
    color: var(--gold); font-size: 22.5px; font-weight: 600;
  }
  .person::after { content: ""; width: 26px; height: 1px; background: var(--gold); margin-top: 2px; }
  .contact { position: absolute; left: 50px; top: 219px; list-style: none; }
  .contact li {
    display: flex; align-items: center; gap: 8px; height: 22px; margin-bottom: 9px;
    color: var(--ink); font-size: 14px;
  }
  .contact svg { width: 18px; height: 18px; flex: none; }

  .globe {
    position: absolute; left: 382px; top: 9px; width: 348px; height: 348px; border-radius: 50%;
    background: radial-gradient(circle at 55% 45%, var(--globe-deep), var(--globe-light) 75%);
    opacity: 0.9;
  }
</style>
</head>
<body>
  <section class="card card--front">
    <div class="network network--upper" role="img" aria-label="Faint connected-dots network pattern"></div>
    <div class="network network--lower" role="img" aria-label="Faint connected-dots network pattern"></div>
    <div class="wordmark"><span>Corvelle Strategies</span><span class="wordmark__sun"></span></div>
    <div class="divider"></div>
    <p class="tagline">STRATEGIC INSIGHT<span class="dot">.</span> CONNECTED IMPACT<span class="dot">.</span></p>
  </section>

  <section class="card card--back">
    <div class="wordmark"><span>Corvelle Strategies</span><span class="wordmark__sun"></span></div>
    <p class="person">Glen Mosswater</p>
    <ul class="contact">
      <li>
        <svg viewBox="0 0 18 18" aria-hidden="true"><circle cx="9" cy="9" r="9" fill="var(--navy)"/><path d="M6 5.2c.4-.3.9-.2 1.1.2l.7 1.3c.2.3.1.7-.2.9l-.5.4c.4.9 1.1 1.7 2 2.1l.4-.5c.2-.3.6-.4.9-.2l1.3.7c.4.2.5.7.2 1.1l-.5.6c-.4.4-1 .5-1.5.3C7.8 11.2 6.6 9.9 5.6 8c-.2-.5-.1-1.1.3-1.5z" fill="#fff"/></svg>
        <span>202-555-0148</span>
      </li>
      <li>
        <svg viewBox="0 0 18 18" aria-hidden="true"><circle cx="9" cy="9" r="9" fill="var(--navy)"/><rect x="5" y="6.3" width="8" height="5.6" rx="0.6" fill="none" stroke="#fff" stroke-width="1"/><path d="M5.2 6.6 9 9.4l3.8-2.8" fill="none" stroke="#fff" stroke-width="1"/></svg>
        <span>glen@corvellestrategies-example.com</span>
      </li>
    </ul>
    <div class="globe" role="img" aria-label="Blue globe illustration wrapped in a network of connected points"></div>
  </section>
</body>
</html>
```